Design some Business Cards for Veltrisa GmbH

doublesided Design...
our old cards are added in the PDFs...
Logosources are also in the ZIP

The new cards must use the old styleguide (Colors, and Fonts and Logo) they should be in a more fashionable design.
Sources must be provided as PSD file, fonst must be added...

The new Company Address and Name is:

Veltrisa GmbH.
Pirolgasse 5
A-9020 Klagenfurt am Wörthersee

For Bernhard Trost:
Name: DI Trost Bernhard, MBA
Position: Geschäftsführer
Phone: +43 676 12 95 07 400
E-Mail: bernhard.trost@veltrisa.example
Web: www.veltrisa.example

For Wolfgang Ebenhoch:
Name: Wolfgang Ebenhoch
Position: Development
Phone: +43 676 12 95 07 300
E-Mail: wolfgang.ebenhoch@veltrisa.example
Web: www.veltrisa.example

```html
<!DOCTYPE html>
<html lang="de">
<head>
<meta charset="utf-8">
<title>Veltrisa GmbH – Visitenkarten</title>
<link rel="stylesheet" href="https://fonts.googleapis.com/css2?family=Arimo:wght@400;700&display=swap">
<style>
  :root {
    --stage: #56595c;
    --card-black: #111111;
    --card-white: #ffffff;
    --brand-orange: #f0781e;
    --text-grey: #6d6d6d;
    --logo-grey: #cfcfcf;
  }
  * { margin: 0; padding: 0; box-sizing: border-box; }
  html, body { width: 1200px; height: 945px; overflow: hidden; }
  body {
    background: var(--stage);
    font-family: "Arimo", Arial, sans-serif;
    position: relative;
  }
  .card {
    position: absolute;
    width: 540px;
    height: 310px;
    box-shadow: 0 10px 24px rgba(0,0,0,0.35);
    overflow: hidden;
  }
  .card--front { left: 90px; top: 170px; display: flex; }
  .card--back {
    left: 570px; top: 465px;
    background: var(--card-black);
    display: flex; align-items: center; justify-content: center;
  }
  .front__brand-panel {
    width: 38%;
    background: var(--card-black);
    display: flex; align-items: center; justify-content: center;
  }
  .front__info {
    flex: 1;
    background: var(--card-white);
    padding: 34px 0 0 26px;
  }
  .wordmark {
    display: flex; align-items: center; gap: 8px;
    color: var(--logo-grey);
    font-weight: 400;
  }
  .wordmark__square { background: var(--brand-orange); display: block; }
  .wordmark--small { font-size: 22px; }
  .wordmark--small .wordmark__square { width: 22px; height: 22px; }
  .wordmark--large { font-size: 40px; gap: 14px; }
  .wordmark--large .wordmark__square { width: 40px; height: 40px; }
  .person__name { color: var(--brand-orange); font-size: 19px; font-weight: 700; }
  .person__role { color: var(--text-grey); font-size: 14px; margin-top: 4px; }
  .contact { list-style: none; margin-top: 22px; }
  .contact__item {
    display: flex; align-items: center; gap: 6px;
    color: var(--text-grey); font-size: 11.5px; line-height: 19px;
  }
  .contact__icon { width: 11px; height: 11px; flex: none; }
  .company { margin-top: 26px; }
  .company__name { color: var(--brand-orange); font-size: 15px; font-weight: 700; }
  .company__address { color: var(--text-grey); font-size: 12.5px; line-height: 17px; margin-top: 6px; font-style: normal; }
</style>
</head>
<body>

<section class="card card--front" aria-label="Visitenkarte Vorderseite">
  <div class="front__brand-panel">
    <div class="wordmark wordmark--small"><span class="wordmark__square"></span>Veltrisa</div>
  </div>
  <div class="front__info">
    <h1 class="person__name">Wolfgang Ebenhoch</h1>
    <p class="person__role">Development</p>
    <ul class="contact">
      <li class="contact__item">
        <svg class="contact__icon" viewBox="0 0 12 12" aria-hidden="true"><circle cx="6" cy="6" r="6" fill="#f0781e"/><path d="M4 3.2l1 1.6-.6.7a4 4 0 0 0 2.1 2.1l.7-.6 1.6 1-.5 1A5 5 0 0 1 3 4z" fill="#fff"/></svg>
        +43 676 12 95 07 300
      </li>
      <li class="contact__item">
        <svg class="contact__icon" viewBox="0 0 12 12" aria-hidden="true"><circle cx="6" cy="6" r="6" fill="#f0781e"/><rect x="3" y="4" width="6" height="4.2" fill="none" stroke="#fff" stroke-width="0.9"/><path d="M3 4l3 2.2L9 4" fill="none" stroke="#fff" stroke-width="0.9"/></svg>
        wolfgang.ebenhoch@veltrisa.example
      </li>
      <li class="contact__item">
        <svg class="contact__icon" viewBox="0 0 12 12" aria-hidden="true"><circle cx="6" cy="6" r="6" fill="#f0781e"/><circle cx="6" cy="6" r="3" fill="none" stroke="#fff" stroke-width="0.9"/><path d="M3 6h6M6 3v6" stroke="#fff" stroke-width="0.7"/></svg>
        www.veltrisa.example
      </li>
    </ul>
    <div class="company">
      <p class="company__name">Veltrisa GmbH.</p>
      <address class="company__address">Pirolgasse 5<br>A-9020 Klagenfurt am Wörthersee</address>
    </div>
  </div>
</section>

<section class="card card--back" aria-label="Visitenkarte Rückseite">
  <div class="wordmark wordmark--large"><span class="wordmark__square"></span>Veltrisa</div>
</section>

</body>
</html>
```